Kid's Cancer Camp Business Card

Create a unique Two-Sided color business cards for Camp Willow Brook, a pediatric cancer camp.

The camp tag line is: Where brave young campers find joy outdoors...

Dale Morrisey, Executive Director
Camp Willow Brook Charitable Foundation, Inc
PO Box 918
Elmstead, NH 06832

Phone - 203-555-0143
Fax - 203-555-0187
Email: dale@campwillowbrook.example
www.campwillowbrook.example

Target Market(s)

Potential Donors, Volunteers and Campers

Industry/Entity Type

Non-profit pediatric cancer camp

Contact Information for Business Card

All contact info that is included in the description

Font styles to use
Other font styles liked:
• Designer chooses font

Requirements
Must have
• Camp Willow Brook Logo and Tag Line
Nice to have
• should be eye catching
Should not have
• not cartoony

```html
<!DOCTYPE html>
<html lang="en">
<head>
<meta charset="utf-8">
<title>Camp Willow Brook – Business Card</title>
<link href="https://fonts.googleapis.com/css2?family=Open+Sans:wght@400;600;700&display=swap" rel="stylesheet">
<style>
  :root {
    --bg: #1c1c1e;
    --card-white: #ffffff;
    --brand-blue: #005ea3;
    --teal: #12a08f;
    --gold: #fbb81f;
    --ink: #222222;
    --logo-blue: #0b5aa6;
  }
  * { box-sizing: border-box; margin: 0; padding: 0; }
  html, body { width: 1200px; height: 1156px; overflow: hidden; }
  body {
    background: var(--bg);
    font-family: "Open Sans", Arial, sans-serif;
    color: var(--ink);
    display: flex;
    flex-direction: column;
    align-items: center;
    justify-content: center;
    gap: 60px;
  }
  .card {
    position: relative;
    width: 840px;
    height: 480px;
    border-bottom: 4px solid var(--gold);
    overflow: hidden;
  }
  .card--front { background: var(--card-white); }
  .card--back { background: var(--brand-blue); }

  .identity { position: absolute; left: 56px; top: 96px; }
  .identity__name { color: var(--teal); font-weight: 700; font-size: 34px; line-height: 1.1; }
  .identity__role, .identity__org { font-size: 15px; line-height: 1.5; }
  .identity__role { margin-top: 6px; }

  .divider {
    position: absolute; left: 56px; right: 56px; top: 212px;
    height: 2px; background: var(--gold);
  }

  .contacts { position: absolute; left: 56px; top: 234px; list-style: none; }
  .contacts li { display: flex; align-items: center; gap: 12px; font-size: 19px; line-height: 36px; }
  .contacts svg { width: 18px; height: 18px; flex: none; }

  .brand { position: absolute; display: flex; align-items: center; gap: 14px; }
  .brand__mark { border-radius: 50%; background: var(--gold); flex: none; }
  .brand__name { font-weight: 700; white-space: nowrap; }

  .card--front .brand { right: 56px; top: 256px; }
  .card--front .brand__mark { width: 40px; height: 40px; }
  .card--front .brand__name { color: var(--logo-blue); font-size: 30px; }

  .address {
    position: absolute; right: 56px; bottom: 44px;
    display: flex; gap: 10px; font-size: 19px; line-height: 1.4;
  }
  .address svg { width: 18px; height: 22px; margin-top: 4px; flex: none; }

  .card--back .brand-block {
    position: absolute; inset: 0;
    display: flex; flex-direction: column; align-items: center; justify-content: center; gap: 14px;
  }
  .card--back .brand { position: static; }
  .card--back .brand__mark { width: 56px; height: 56px; }
  .card--back .brand__name { color: #ffffff; font-size: 48px; }
  .tagline { color: var(--gold); font-size: 20px; }
</style>
</head>
<body>
  <section class="card card--front">
    <div class="identity">
      <h1 class="identity__name">Dale Morrisey</h1>
      <p class="identity__role">Executive Director</p>
      <p class="identity__org">Camp Willow Brook Charitable Foundation, Inc</p>
    </div>
    <div class="divider"></div>
    <ul class="contacts">
      <li>
        <svg viewBox="0 0 24 24" aria-hidden="true"><path fill="#12a08f" d="M6.6 10.8a15 15 0 0 0 6.6 6.6l2.2-2.2a1 1 0 0 1 1-.25 11.4 11.4 0 0 0 3.6.57 1 1 0 0 1 1 1V20a1 1 0 0 1-1 1A17 17 0 0 1 3 4a1 1 0 0 1 1-1h3.5a1 1 0 0 1 1 1c0 1.250.2 2.450.57 3.6a1 1 0 0 1-.25 1z"/></svg>
        203-555-0143
      </li>
      <li>
        <svg viewBox="0 0 24 24" aria-hidden="true"><path fill="#12a08f" d="M6 2h12v6H6zM3 9h18v9h-3v4H6v-4H3zm5 6v5h8v-5z"/></svg>
        203-555-0187
      </li>
      <li>
        <svg viewBox="0 0 24 24" aria-hidden="true"><path fill="#12a08f" d="M2 5h20v14H2zm2 2v.5l8 5 8-5V7z"/></svg>
        dale@campwillowbrook.example
      </li>
      <li>
        <svg viewBox="0 0 24 24" aria-hidden="true"><circle cx="12" cy="12" r="9" fill="none" stroke="#12a08f" stroke-width="2"/><path d="M3 12h18M12 3c3 3 3 15 0 18M12 3c-3 3-3 15 0 18" fill="none" stroke="#12a08f" stroke-width="1.5"/></svg>
        www.campwillowbrook.example
      </li>
    </ul>
    <div class="brand">
      <span class="brand__mark"></span>
      <span class="brand__name">Camp Willow Brook</span>
    </div>
    <div class="address">
      <svg viewBox="0 0 20 26" aria-hidden="true"><path fill="#fbb81f" d="M10 0a10 10 0 0 0-10 10c0 7 10 16 10 16s10-9 10-16A10 10 0 0 0 10 0zm0 14a4 4 0 1 1 0-8 4 4 0 0 1 0 8z"/></svg>
      <p>PO Box 918<br>Elmstead, NH 06832</p>
    </div>
  </section>

  <section class="card card--back">
    <div class="brand-block">
      <div class="brand">
        <span class="brand__mark"></span>
        <span class="brand__name">Camp Willow Brook</span>
      </div>
      <p class="tagline">Where brave young campers find joy outdoors</p>
    </div>
  </section>
</body>
</html>
```